Creative Brief
Marketing Collateral for Real Estate Business
Create matching postcards and Business Card.
MARKETING COLLATERAL FOR REAL ESTATE COMPANY
Create matching postcards, HTML email template and Business Card.
Postcard (5.5” x 8.5”) template
Email HTML template
Business Card
DESCRIPTION
Our office needs 2-3 “Just Listed” postcard templates for REAL ESTATE FORECLOSURE LISITNGS. The templates must display two logos which are provided (FindMarlowHomesteads.example to be large in size). We need the ability to insert pictures of each new listing inside within the template. The design must be colorful (earth tone colors), professional, simple and eye catching. Postcard: We also want 1-2 generic postcard templates where a standard/general real estate picture is already inserted which can be used for multiple/different properties.
Postcard templates must meet the printing specifications for PressNook.example. The templates must be provided in digital formats that are editable by the project holder. They must also be provided in print ready formats. Our company is based in Charleston, SC, USA. Please view images of Charleston, SC, USA via google if necessary for the postcard template.
The HTML Email Template(s) will be used to mass email our database with new listings.
Real Estate
Buyers of Real Estate Foreclosed Properties; Real Estate Investors.
DESIGN
POSTCARD COMMENTS / STATEMENTS TO BE INCLUDED WITHIN THE POSTCARD / EMAIL HTML
-PRE-LISTING(1-2 Templates)
-JUST LISTED (1-2 Templates)
-SEARCH HUNDREDS OF BANK OWNED FORECLOSURES – SIGN UP FREE! FINDMARLOWHOMESTEADS.EXAMPLE
-Join FindMarlowHomesteads.example and be the first to know about newly listed Charleston Foreclosures.
-Don’t miss this opportunity to buy a bank owned foreclosure.
-We are your Charleston Foreclosure Specialist!
-NEW LISTING ALERT – Sign up and receive listings meeting your criteria today! (in a highlighted icon or box or similar)
-This property is NOT listed in MLS yet. Please contact me if you are interested in purchasing this property. (disclaimer/small font))
POSTCARD SIZE
Postcard 5.5” x 8.5”
COLORS
Blue / Green / Tan (Earth tone colors) / To match FindMarlowHomesteads.example logo
Color (front and back)
Images and Date to be used

```html
<!DOCTYPE html>
<html lang="en">
<head>
<meta charset="utf-8">
<title>Foreclosure Marketing Collateral</title>
<link rel="stylesheet" href="https://fonts.googleapis.com/css2?family=Arimo:wght@400;700&family=Oswald:wght@500;700&display=swap">
<style>
:root{
  --blue:#1f4e8c;
  --blue-dark:#163a6b;
  --green:#6cb33f;
  --green-dark:#4e8f2a;
  --sky:#8fb9e0;
  --tan:#c9b48f;
  --paper:#ffffff;
  --ink:#2b2b2b;
  --muted:#6b6b6b;
  --stage:#ece7dd;
  --label:#3a3a3a;
}
*{box-sizing:border-box;margin:0;padding:0}
html,body{width:1200px;height:553px;overflow:hidden}
body{background:var(--stage);font-family:"Arimo",Arial,sans-serif;color:var(--ink);position:relative}
.label{position:absolute;font-size:11px;font-weight:700;color:var(--label)}
.piece{position:absolute;background:var(--paper);overflow:hidden;box-shadow:0 1px 3px rgba(0,0,0,.25)}
.photo{position:absolute}
.photo--house{background:linear-gradient(180deg,#9cc3e6 0%,#cfdfe9 45%,#b7a585 70%,#6f8f4a 100%)}
.photo--agent{background:linear-gradient(180deg,#2b2b2b 0%,#3a3a3a 35%,#c7a48a 36%,#d8b79e 60%,#2a2a2a 61%,#1e1e1e 100%);border-radius:40% 40% 0 0}
.photo--thumb{background:linear-gradient(180deg,#a8c8e4,#b9a47f 70%,#6f8f4a)}
.brand{position:absolute;display:flex;align-items:center;gap:4px;font-weight:700;color:var(--blue);white-space:nowrap}
.brand__mark{background:var(--green);flex:none}
.partner{position:absolute;font-family:"Oswald",sans-serif;font-weight:500;letter-spacing:2px;color:var(--blue);white-space:nowrap}

/* postcard front */
.front .topbar{position:absolute;left:0;top:0;width:100%;height:8px;background:var(--blue)}
.front .brand{left:10px;top:16px;font-size:9px}
.front .brand__mark{width:14px;height:14px}
.front .headline{position:absolute;left:12px;top:58px;font-family:"Oswald",sans-serif;font-weight:700;line-height:.95}
.front .headline b{display:block;font-size:28px;color:var(--green)}
.front .headline b+b{color:var(--blue)}
.front .headline small{display:block;font-family:"Arimo",sans-serif;font-size:8px;font-weight:700;color:var(--blue);margin-top:3px;letter-spacing:.5px}
.front .preview{position:absolute;left:14px;top:142px;width:110px;height:28px;background:#f3f5f7;border:1px solid #cfd6de;display:flex;gap:4px;padding:3px}
.front .preview .photo{position:static;width:30px;height:20px}
.front .preview span{font-size:5px;color:var(--muted);line-height:1.3}
.front .band-green{position:absolute;left:0;bottom:56px;width:100%;height:6px;background:var(--green)}
.front .band{position:absolute;left:0;bottom:0;width:100%;height:56px;background:var(--blue);color:#fff;font-size:10px;line-height:1.35;padding:10px 12px 0 150px;text-align:right}
.front .band strong{font-weight:700}

/* postcard back */
.back .half{position:absolute;top:0;height:100%}
.back .left{left:0;width:50%}
.back .right{left:50%;width:50%;border-left:1px dashed #c9c9c9}
.back .alert{position:absolute;left:10px;top:70px;font-family:"Oswald",sans-serif;font-weight:700;font-size:19px;color:var(--green)}
.back .points{position:absolute;left:10px;top:100px;width:176px;display:flex;gap:8px}
.back .points p{flex:1;font-size:7px;line-height:1.35;color:var(--blue);font-weight:700}
.back .points p::before{content:"";display:inline-block;width:5px;height:5px;background:var(--green);margin-right:3px}
.back .right .brand{left:8px;top:8px;font-size:6px}
.back .right .brand__mark{width:10px;height:10px}
.back .contact{position:absolute;left:8px;top:24px;font-size:5px;color:var(--muted);line-height:1.4}
.back .stamp{position:absolute;right:8px;top:8px;width:28px;height:32px;border:1px solid #b5b5b5}
.back .mailto{position:absolute;left:30px;top:92px;width:140px}
.back .mailto i{display:block;height:1px;background:#c5c5c5;margin-bottom:11px}
.back .partner{right:20px;top:150px;font-size:12px}
.back .disclaimer{position:absolute;left:8px;top:172px;width:176px;font-size:4.5px;color:var(--muted)}
.back .band-green{position:absolute;left:0;bottom:58px;width:100%;height:5px;background:var(--green)}
.back .band{position:absolute;left:0;bottom:0;width:100%;height:58px;background:var(--blue);color:#fff;font-family:"Oswald",sans-serif;font-weight:500;font-size:14px;padding:20px 0 0 90px}

.back--ribbon .alert{left:0;top:62px;background:var(--green);color:#fff;padding:2px 10px;font-size:17px}

/* business cards */
.card{width:178px;height:82px}
.card .swoosh{position:absolute;left:0;bottom:0;width:100%;height:14px;background:var(--blue)}
.card .swoosh::before{content:"";position:absolute;left:0;top:-4px;width:100%;height:4px;background:var(--green)}
.card .brand{left:8px;top:10px;font-size:5.5px}
.card .brand__mark{width:10px;height:10px}
.card .who{position:absolute;left:8px;top:32px;font-size:6px;line-height:1.45;color:var(--muted)}
.card .who b{color:var(--blue);font-size:7px}
.card .photo--agent{right:10px;top:8px;width:36px;height:46px;border-radius:2px}
.card--green{background:var(--green)}
.card--blue{background:var(--blue)}
.card--green .partner,.card--blue .partner{color:#fff;left:0;right:0;top:30px;text-align:center;font-size:14px}
.card--plain{background:#fff}
.card--plain .partner{left:0;right:0;top:30px;text-align:center;font-size:14px}
.card--green .rule,.card--blue .rule{position:absolute;left:40px;right:40px;top:52px;height:1px;background:rgba(255,255,255,.6)}

.sig{width:178px;height:72px}
.sig .brand{left:8px;top:10px;font-size:5.5px}
.sig .brand__mark{width:10px;height:10px}
.sig .who{position:absolute;left:8px;top:28px;font-size:6px;line-height:1.45;color:var(--muted)}
.sig .who b{color:var(--blue)}
.sig .photo--agent{right:10px;top:8px;width:32px;height:44px;border-radius:2px}
.sig .strip{position:absolute;left:0;bottom:0;width:100%;height:8px;background:var(--green)}
</style>
</head>
<body>

<span class="label" style="left:10px;top:6px">Front</span>
<span class="label" style="left:410px;top:6px">Front</span>

<section class="piece front" style="left:10px;top:22px;width:388px;height:240px">
  <div class="photo photo--house" role="img" aria-label="Charleston style house with front lawn" style="left:150px;top:8px;width:238px;height:170px"></div>
  <div class="topbar"></div>
  <div class="brand" style="background:#fff;padding:4px 6px;left:4px;top:12px"><span class="brand__mark"></span>FindMarlowHomesteads.example</div>
  <div class="photo photo--agent" role="img" aria-label="Real estate agent holding a folder" style="left:255px;top:40px;width:70px;height:138px"></div>
  <div class="headline"><b>SEARCH</b><b>HUNDREDS</b><small>OF BANK OWNED FORECLOSURES</small></div>
  <div class="preview"><div class="photo photo--thumb" role="img" aria-label="Listing thumbnail"></div><span>3 bed · 2 bath<br>Bank owned home</span></div>
  <div class="band-green"></div>
  <div class="band"><strong>Join FindMarlowHomesteads.example</strong><br>and be the first to know about newly listed Charleston Foreclosures.</div>
</section>

<section class="piece front" style="left:410px;top:22px;width:388px;height:240px">
  <div class="photo photo--house" role="img" aria-label="Charleston home exterior at sunset" style="left:130px;top:8px;width:258px;height:170px"></div>
  <div class="topbar"></div>
  <div class="brand" style="background:#fff;padding:4px 6px;left:4px;top:12px"><span class="brand__mark"></span>FindMarlowHomesteads.example</div>
  <div class="photo photo--agent" role="img" aria-label="Real estate agent holding a folder" style="left:270px;top:40px;width:70px;height:138px"></div>
  <div class="headline"><b>SEARCH</b><b>HUNDREDS</b><small>OF BANK OWNED FORECLOSURES</small></div>
  <div class="preview"><div class="photo photo--thumb" role="img" aria-label="Listing thumbnail"></div><span>4 bed · 3 bath<br>Bank owned home</span></div>
  <div class="band-green"></div>
  <div class="band"><strong>Join FindMarlowHomesteads.example</strong><br>and be the first to know about newly listed Charleston Foreclosures.</div>
</section>

<span class="label" style="left:10px;top:270px">Back</span>
<span class="label" style="left:410px;top:270px">Back</span>

<section class="piece back" style="left:10px;top:286px;width:388px;height:250px">
  <div class="half left">
    <div class="photo photo--house" role="img" aria-label="Row of listed homes" style="left:0;top:0;width:100%;height:60px"></div>
    <div class="alert">NEW LISTING ALERT</div>
    <div class="points"><p>SIGN UP and receive listings meeting your criteria today!</p><p>DON'T MISS this opportunity to buy a bank owned foreclosure.</p></div>
  </div>
  <div class="half right">
    <div class="brand"><span class="brand__mark"></span>FindMarlowHomesteads.example</div>
    <div class="contact">Dana Whitfield<br>(843) 555-0142<br>dana@findmarlowhomesteads.example<br>120 Harbor Row, Suite 4</div>
    <div class="stamp"></div>
    <div class="mailto"><i></i><i></i><i></i></div>
    <div class="partner">HOLLINS</div>
    <div class="disclaimer">This property is NOT listed in MLS yet. Please contact me if you are interested.</div>
  </div>
  <div class="band-green"></div>
  <div class="band">We are your Charleston Foreclosure Specialist!</div>
  <div class="photo photo--agent" role="img" aria-label="Smiling real estate agent portrait" style="left:14px;top:186px;width:54px;height:64px"></div>
</section>

<section class="piece back back--ribbon" style="left:410px;top:286px;width:388px;height:250px">
  <div class="half left">
    <div class="photo photo--house" role="img" aria-label="Foreclosed home for sale" style="left:0;top:0;width:100%;height:56px"></div>
    <div class="alert">NEW LISTING ALERT</div>
    <div class="points"><p>SIGN UP and receive listings meeting your criteria today!</p><p>DON'T MISS this opportunity to buy a bank owned foreclosure.</p></div>
  </div>
  <div class="half right">
    <div class="brand"><span class="brand__mark"></span>FindMarlowHomesteads.example</div>
    <div class="contact">Dana Whitfield<br>(843) 555-0142<br>dana@findmarlowhomesteads.example<br>120 Harbor Row, Suite 4</div>
    <div class="stamp"></div>
    <div class="mailto"><i></i><i></i><i></i></div>
    <div class="partner">HOLLINS</div>
    <div class="disclaimer">This property is NOT listed in MLS yet. Please contact me if you are interested.</div>
  </div>
  <div class="band-green"></div>
  <div class="band">We are your Charleston Foreclosure Specialist!</div>
  <div class="photo photo--agent" role="img" aria-label="Smiling real estate agent portrait" style="left:14px;top:186px;width:54px;height:64px"></div>
</section>

<span class="label" style="left:806px;top:6px">Business Card Front</span>
<span class="label" style="left:994px;top:6px">Business Card Front</span>
<div class="piece card" style="left:806px;top:22px">
  <div class="brand"><span class="brand__mark"></span>FindMarlowHomesteads.example</div>
  <div class="who"><b>Dana Whitfield</b><br>Foreclosure Specialist<br>(843) 555-0142</div>
  <div class="photo photo--agent" role="img" aria-label="Agent headshot"></div>
  <div class="swoosh"></div>
</div>
<div class="piece card" style="left:994px;top:22px">
  <div class="brand"><span class="brand__mark"></span>FindMarlowHomesteads.example</div>
  <div class="who"><b>Dana Whitfield</b><br>Foreclosure Specialist<br>(843) 555-0142</div>
  <div class="photo photo--agent" role="img" aria-label="Agent headshot"></div>
  <div class="swoosh"></div>
</div>

<span class="label" style="left:806px;top:110px">Business Card Front</span>
<span class="label" style="left:994px;top:110px">Business Card Front</span>
<div class="piece card" style="left:806px;top:126px">
  <div class="brand"><span class="brand__mark"></span>FindMarlowHomesteads.example</div>
  <div class="who"><b>Dana Whitfield</b><br>Foreclosure Specialist<br>(843) 555-0142</div>
  <div class="photo photo--agent" role="img" aria-label="Agent headshot"></div>
  <div class="swoosh"></div>
</div>
<div class="piece card" style="left:994px;top:126px">
  <div class="brand"><span class="brand__mark"></span>FindMarlowHomesteads.example</div>
  <div class="who"><b>Dana Whitfield</b><br>Foreclosure Specialist<br>(843) 555-0142</div>
  <div class="photo photo--agent" role="img" aria-label="Agent headshot"></div>
  <div class="swoosh"></div>
</div>

<span class="label" style="left:806px;top:214px">Business Card Back</span>
<span class="label" style="left:994px;top:214px">Business Card Back</span>
<div class="piece card card--green" style="left:806px;top:230px"><div class="partner">HOLLINS</div><div class="rule"></div></div>
<div class="piece card card--blue" style="left:994px;top:230px"><div class="partner">HOLLINS</div><div class="rule"></div></div>
<div class="piece card card--green" style="left:806px;top:322px"><div class="partner">HOLLINS</div><div class="rule"></div></div>
<div class="piece card card--blue" style="left:994px;top:322px"><div class="partner">HOLLINS</div><div class="rule"></div></div>

<span class="label" style="left:806px;top:448px">Email Signature</span>
<span class="label" style="left:994px;top:448px">Email Signature</span>
<div class="piece sig" style="left:806px;top:464px">
  <div class="brand"><span class="brand__mark"></span>FindMarlowHomesteads.example</div>
  <div class="who"><b>Dana Whitfield</b><br>(843) 555-0142<br>dana@findmarlowhomesteads.example</div>
  <div class="photo photo--agent" role="img" aria-label="Agent headshot"></div>
  <div class="strip"></div>
</div>
<div class="piece sig" style="left:994px;top:464px">
  <div class="brand"><span class="brand__mark"></span>FindMarlowHomesteads.example</div>
  <div class="who"><b>Dana Whitfield</b><br>(843) 555-0142<br>dana@findmarlowhomesteads.example</div>
  <div class="photo photo--agent" role="img" aria-label="Agent headshot"></div>
  <div class="strip"></div>
</div>

</body>
</html>
```